Anselm business card

Business card for commercial photography , photographer specialized in advertising, architecture and interior photography, adventure imagery and camera work. 40 years old, worked for the last 20 years. Business card needs to convey a sense of confidence in work achieved. Card needs to be eye catching as will be left behind in many people's offices. Should also mention discreetly NLVG accredited photographer at the verso of the card. Phone number and website link must be apparent easily.

Target Market(s)

Advertising agencies, commercial photography representation

Industry/Entity Type

Architecture

Contact Information for Business Card

Phone number : +61 470 918 264
anselm.varnet@mailbrook.net
www.anselmvarnet.net

Font styles to use
Sans Serif

Requirements
Must have
• Email adress
• Website
• Phone number
• Name
• Photographer
Nice to have
• NLVG accredited photographer
Should not have
• Rond corners

```html
<!DOCTYPE html>
<html lang="en">
<head>
<meta charset="utf-8">
<title>Anselm Varnet Photography – Business Card</title>
<link rel="stylesheet" href="https://fonts.googleapis.com/css2?family=Cinzel:wght@400;500&family=Raleway:wght@400;500&display=swap">
<style>
  :root {
    --canvas: #e9e7e3;
    --ink: #232323;
    --ink-deep: #1c1c1c;
    --paper: #ffffff;
    --teal: #36bfb3;
    --light: #f2f2f2;
    --muted: #9a9a9a;
  }
  * { margin: 0; padding: 0; box-sizing: border-box; }
  html, body {
    width: 1200px; height: 784px; overflow: hidden;
    background: var(--canvas);
  }
  .canvas { position: relative; width: 1200px; height: 784px; }

  .card {
    position: absolute; width: 600px; height: 350px; overflow: hidden;
    box-shadow: 0 6px 18px rgba(0,0,0,.18);
  }
  .card-front { left: 60px; top: 50px; background: var(--ink); }
  .card-back { left: 540px; top: 384px; background: var(--paper); }

  .brand { position: absolute; text-align: center; }
  .brand-mark { display: block; margin: 0 auto; border-radius: 50%; }
  .brand-name {
    font-family: "Cinzel", serif; font-weight: 400;
    font-size: 34px; letter-spacing: 1px; line-height: 1; white-space: nowrap;
  }
  .brand-tagline {
    font-family: "Cinzel", serif; font-weight: 400; color: var(--teal);
    font-size: 13px; letter-spacing: 13px; line-height: 1; margin-top: 6px;
    padding-left: 13px; white-space: nowrap;
  }

  .card-front .brand { left: 150px; top: 42px; width: 300px; }
  .card-front .brand-mark { width: 104px; height: 104px; background: var(--teal); margin-bottom: 14px; }
  .card-front .brand-name { color: var(--light); }

  .card-back .swoosh { position: absolute; inset: 0; }
  .card-back .brand { left: 40px; top: 30px; width: 330px; }
  .card-back .brand-mark { width: 96px; height: 96px; background: var(--ink-deep); margin-bottom: 12px; }
  .card-back .brand-name { color: var(--ink-deep); }

  .contact {
    position: absolute; left: 318px; top: 214px; list-style: none;
    font-family: "Raleway", sans-serif; color: var(--light); font-size: 15px;
  }
  .contact li { display: flex; align-items: center; gap: 8px; height: 27px; }
  .contact svg { width: 16px; height: 16px; flex: none; }
  .contact .phone { font-size: 17px; }

  .accreditation {
    position: absolute; right: 22px; top: 196px; width: 74px; text-align: left;
    font-family: "Raleway", sans-serif; color: var(--light);
  }
  .accreditation-badge { width: 48px; height: 20px; background: var(--light); border-radius: 3px; }
  .accreditation-text { font-size: 6.5px; letter-spacing: .6px; line-height: 1.25; margin-top: 5px; text-transform: uppercase; }
</style>
</head>
<body>
<main class="canvas">

  <section class="card card-front" aria-label="Card front">
    <div class="brand">
      <span class="brand-mark"></span>
      <p class="brand-name">Anselm Varnet</p>
      <p class="brand-tagline">Photography</p>
    </div>
  </section>

  <section class="card card-back" aria-label="Card back">
    <svg class="swoosh" viewBox="0 0 600 350" preserveAspectRatio="none" aria-hidden="true">
      <path d="M0 350 L0 318 C170 300 330 250 450 160 C520 108 570 60 600 28 L600 350 Z" fill="var(--ink)"/>
      <path d="M330 178 C450 140 540 80 600 18 L600 46 C540 100 450 152 330 178 Z" fill="var(--teal)"/>
    </svg>

    <div class="brand">
      <span class="brand-mark"></span>
      <p class="brand-name">Anselm Varnet</p>
      <p class="brand-tagline">Photography</p>
    </div>

    <ul class="contact">
      <li class="phone">
        <svg viewBox="0 0 16 16"><path fill="var(--teal)" d="M3.2 1.5 5.6 1 7 4.6 5.5 5.8c.8 1.8 2.1 3.1 3.9 4L10.6 8.3 14.2 9.8 13.7 12.2C13.5 13.3 12.6 14 11.5 14 6 13.7 2.3 10 2 4.5 2 3.4 2.4 1.8 3.2 1.5Z"/></svg>
        +61 470 918 264
      </li>
      <li>
        <svg viewBox="0 0 16 16"><rect x="1" y="3.5" width="14" height="9.5" rx="1" fill="var(--teal)"/><path d="M1.5 4 8 9l6.5-5" stroke="var(--ink)" stroke-width="1.3" fill="none"/></svg>
        anselm.varnet@mailbrook.net
      </li>
      <li>
        <svg viewBox="0 0 16 16"><circle cx="8" cy="8" r="7" fill="var(--teal)"/><g stroke="var(--ink)" stroke-width="1" fill="none"><ellipse cx="8" cy="8" rx="3" ry="7"/><path d="M1 8h14M2.2 4.5h11.6M2.2 11.5h11.6"/></g></svg>
        www.anselmvarnet.net
      </li>
    </ul>

    <div class="accreditation">
      <div class="accreditation-badge"></div>
      <p class="accreditation-text">NLVG accredited professional photographer</p>
    </div>
  </section>

</main>
</body>
</html>
```